Responsive Web Designer Required For A Fashion ECommerce Project

We need top professional Graphic/Web designers to create responsive web design page for an enterprise ecommerce website so as to set it apart from the competition.
The final output designs for all the breakpoints will be delivered as pixel-perfect PSD files.
The final design output must be clean and present a modern look and feel, and the elements should be consistent throughout the design. The end product design must be professional to reinforce the client as a contemporary and trusted organization.
1. Home Page
2. Category Page
3. Product Page
4. Check Out Page
5. Account Dashboard
6. Deals of the Week
7. Special Offers
8. Featured Products
9. Most Wanted
10.Loyalty Rewards
11. Order Confirmation
12. Stylist Picks
All the best!
Industry/Entity Type
Fashion
Number of Pages Required
5+ page
Look and feel
Each slider illustrates characteristics of the customer's brand and the style your logo design should communicate.

```html
<!DOCTYPE html>
<html lang="en">
<head>
<meta charset="utf-8">
<title>Modalise in UK</title>
<link href="https://fonts.googleapis.com/css2?family=Raleway:wght@400;500;600;700&family=Questrial&display=swap" rel="stylesheet">
<style>
:root{
  --cyan:#2ec9dc;
  --cyan-dark:#1fb6cb;
  --ink:#222;
  --muted:#888;
  --line:#e2e2e2;
  --footer:#0d0d0d;
  --footer-bar:#1c1c1c;
  --yellow:#f6b52a;
  --white:#fff;
}
*{margin:0;padding:0;box-sizing:border-box}
html,body{width:749px;height:1200px;overflow:hidden;background:var(--white)}
body{position:relative;font-family:'Raleway',sans-serif;color:var(--ink)}
.abs{position:absolute}

/* header */
.top-links{top:8px;right:130px;font-size:7px;color:var(--muted);display:flex;gap:4px;align-items:center}
.top-links svg{width:10px;height:9px}
.brand{left:120px;top:27px;font-family:'Questrial',sans-serif;font-size:20px;color:var(--ink)}
.search{left:488px;top:40px;width:142px;height:19px;border:1px solid #d6d6d6;background:#fafafa;display:flex}
.search span{flex:1;font-size:6px;font-style:italic;color:var(--muted);padding:6px 6px}
.search i{width:20px;border-left:1px solid #d6d6d6;display:flex;align-items:center;justify-content:center}

/* nav */
.nav{left:0;top:69px;width:749px;height:28px;background:linear-gradient(#3fd3e4,var(--cyan-dark))}
.nav a{position:absolute;top:0;line-height:28px;font-size:7.5px;font-weight:600;color:var(--white);text-decoration:none;transform:translateX(-50%);white-space:nowrap}
.nav b{position:absolute;top:0;width:1px;height:28px;background:rgba(255,255,255,.45)}

/* hero */
.hero{left:0;top:97px;width:749px;height:276px;background:radial-gradient(ellipse at 50% 45%,#b8b8b8,#6a6a6a 55%,#3a3a3a)}
.hero h1{position:absolute;top:97px;width:100%;text-align:center;font-size:26px;font-weight:700;color:var(--white);letter-spacing:.2px}
.hero h2{position:absolute;top:131px;width:100%;text-align:center;font-size:14.5px;font-weight:700;color:var(--white)}
.hero svg.arrow{position:absolute;top:108px;width:14px;height:26px}
.dots{position:absolute;top:259px;left:353px;display:flex;gap:3px}
.dots span{width:9px;height:9px;border-radius:50%;background:var(--white)}

/* tiles */
.tile{top:388px;width:167px;height:111px;border:1px solid #ccc}
.tile .pic{height:84px}
.tile .label{height:26px;line-height:26px;text-align:center;color:var(--white);font-size:11px;font-weight:500}

/* sections */
.section-title{left:116px;width:516px;display:flex;align-items:center;gap:10px;font-size:12.5px;font-weight:500;letter-spacing:1.6px}
.section-title::before,.section-title::after{content:"";flex:1;height:3px;background:#f0f0f0}
.section-title.alt{color:var(--cyan)}
.row{left:118px;width:513px;display:flex;justify-content:space-between}
.card{width:124px;height:158px;border:1px solid var(--line);position:relative;background:var(--white)}
.card .pic{position:absolute;left:22px;top:14px;width:80px;height:60px;border-radius:6px}
.card h3{position:absolute;top:102px;width:100%;text-align:center;font-size:8.5px;font-weight:500}
.card p{position:absolute;top:114px;width:100%;text-align:center;font-size:5.6px;color:var(--muted)}
.card .price{position:absolute;left:13px;top:134px;font-size:9px;color:var(--cyan)}
.card .cart{position:absolute;right:12px;top:131px;width:50px;height:14px;background:#1b1b1b;color:var(--white);font-size:5.8px;line-height:14px;text-align:center}
.chev{width:12px;height:26px}

/* footer */
.footer{left:0;top:1005px;width:749px;height:159px;background:var(--footer);color:var(--white)}
.col{position:absolute;top:35px}
.col h4{font-size:9px;font-weight:500;margin-bottom:5px;letter-spacing:.2px}
.col li{list-style:none;font-size:6.3px;color:#bbb;line-height:13.2px}
.news p{font-size:6.3px;color:#bbb;margin-bottom:6px}
.news .field{width:140px;height:17px;background:var(--white);color:#999;font-size:5.5px;padding:6px 8px}
.news .btn{margin-top:5px;width:60px;height:17px;background:var(--cyan);font-size:6.5px;font-weight:600;text-align:center;line-height:17px}
.bar{left:0;top:1164px;width:749px;height:36px;background:var(--footer-bar)}
.bar small{position:absolute;left:124px;top:14px;font-size:5.8px;color:#777}
.social{position:absolute;left:587px;top:11px;display:flex;gap:3px}
.social span{width:11px;height:11px;background:var(--white);border-radius:2px}
</style>
</head>
<body>

<div class="abs top-links">
  <span>My Account</span><span>|</span><span>Sign Up</span><span>|</span><span>Login</span><span>|</span><span>My Cart</span>
  <svg viewBox="0 0 10 9"><path d="M0 1h2l1.3 5h5L10 2H3" fill="none" stroke="#999" stroke-width="1.2"/><circle cx="4" cy="8" r=".9" fill="#999"/><circle cx="8" cy="8" r=".9" fill="#999"/></svg>
</div>
<div class="abs brand">Modalise in UK</div>
<div class="abs search"><span>Search here</span><i><svg width="9" height="9" viewBox="0 0 9 9"><circle cx="3.7" cy="3.7" r="2.8" fill="none" stroke="#999" stroke-width="1"/><path d="M5.8 5.8 8.5 8.5" stroke="#999" stroke-width="1.2"/></svg></i></div>

<nav class="abs nav">
  <a style="left:146px">HOME</a><b style="left:178px"></b>
  <a style="left:213px">ABOUT US</a><b style="left:250px"></b>
  <a style="left:298px">NEW ARRIVALS</a><b style="left:346px"></b>
  <a style="left:410px">FASHION ACCESSORIES</a><b style="left:472px"></b>
  <a style="left:510px">APPARELS</a><b style="left:548px"></b>
  <a style="left:586px">BUY NOW</a>
</nav>

<section class="abs hero" role="img" aria-label="Black and white photo of a model wearing large white sunglasses">
  <h1>FASHION ACCESORIES &amp; APPAREL</h1>
  <h2>MAURIS VEL LACUS FELIS VESTIBULUM</h2>
  <svg class="arrow" style="left:106px" viewBox="0 0 14 26"><path d="M12 2 2 13l10 11" fill="none" stroke="#fff" stroke-width="3"/></svg>
  <svg class="arrow" style="left:628px" viewBox="0 0 14 26"><path d="M2 2l10 11L2 24" fill="none" stroke="#fff" stroke-width="3"/></svg>
  <div class="dots"><span></span><span></span><span></span><span></span></div>
</section>

<div class="abs tile" style="left:119px"><div class="pic" role="img" aria-label="Red handbag with yellow heels" style="background:linear-gradient(135deg,#eee,#d9553a 60%,#e9c13a)"></div><div class="label" style="background:#3a3a3a">LATEST FASHION</div></div>
<div class="abs tile" style="left:291px"><div class="pic" role="img" aria-label="Beige bag with pink scarf and sunglasses" style="background:linear-gradient(135deg,#f2f2f2,#cdbfa8 55%,#c97a86)"></div><div class="label" style="background:var(--cyan)">APPARELS</div></div>
<div class="abs tile" style="left:463px"><div class="pic" role="img" aria-label="Orange handbag with yellow shoe" style="background:linear-gradient(135deg,#f08a1e,#f5a623 60%,#f7e7a8)"></div><div class="label" style="background:var(--yellow)">SHOP NOW</div></div>

<h2 class="abs section-title" style="top:527px">FEATURED ITEMS</h2>
<svg class="abs chev" style="left:96px;top:619px" viewBox="0 0 12 26"><path d="M10 1 2 13l8 12" fill="none" stroke="#aaa"/></svg>
<svg class="abs chev" style="left:641px;top:619px" viewBox="0 0 12 26"><path d="M2 1l8 12-8 12" fill="none" stroke="#aaa"/></svg>
<div class="abs row" style="top:562px">
  <div class="card"><div class="pic" role="img" aria-label="Dark sunglasses" style="background:linear-gradient(#fff,#d8d8e4 50%,#fff)"></div><h3>Product Name</h3><p>Morbi diam mauris viverra in gravid</p><span class="price">£57.58</span><span class="cart">Add to Cart</span></div>
  <div class="card"><div class="pic" role="img" aria-label="Brown handbag with scarf" style="background:linear-gradient(#fff,#b9a48c 50%,#fff)"></div><h3>Product Name</h3><p>Morbi diam mauris viverra in gravid</p><span class="price">£57.58</span><span class="cart">Add to Cart</span></div>
  <div class="card"><div class="pic" role="img" aria-label="Orange bag with beads" style="background:linear-gradient(#fff,#f08c3c 50%,#fff)"></div><h3>Product Name</h3><p>Morbi diam mauris viverra in gravid</p><span class="price">£57.58</span><span class="cart">Add to Cart</span></div>
  <div class="card"><div class="pic" role="img" aria-label="Brown shoulder bag" style="background:linear-gradient(#fff,#8a5a3a 50%,#fff)"></div><h3>Product Name</h3><p>Morbi diam mauris viverra in gravid</p><span class="price">£57.58</span><span class="cart">Add to Cart</span></div>
</div>

<h2 class="abs section-title alt" style="top:766px">BEST SELINGS</h2>
<svg class="abs chev" style="left:96px;top:864px" viewBox="0 0 12 26"><path d="M10 1 2 13l8 12" fill="none" stroke="#aaa"/></svg>
<svg class="abs chev" style="left:641px;top:864px" viewBox="0 0 12 26"><path d="M2 1l8 12-8 12" fill="none" stroke="#aaa"/></svg>
<div class="abs row" style="top:801px">
  <div class="card"><div class="pic" role="img" aria-label="Black jewelled bracelet" style="background:linear-gradient(#fff,#7a7a7a 50%,#fff)"></div><h3>Product Name</h3><p>Morbi diam mauris viverra in gravid</p><span class="price">£57.58</span><span class="cart">Add to Cart</span></div>
  <div class="card"><div class="pic" role="img" aria-label="Pink bangles" style="background:linear-gradient(#fff,#ec5b9c 50%,#fff)"></div><h3>Product Name</h3><p>Morbi diam mauris viverra in gravid</p><span class="price">£57.58</span><span class="cart">Add to Cart</span></div>
  <div class="card"><div class="pic" role="img" aria-label="Turquoise beaded necklace" style="background:linear-gradient(#fff,#5bbfc4 45%,#e08a4a 60%,#fff)"></div><h3>Product Name</h3><p>Morbi diam mauris viverra in gravid</p><span class="price">£57.58</span><span class="cart">Add to Cart</span></div>
  <div class="card"><div class="pic" role="img" aria-label="Black high heel shoe and bag" style="background:linear-gradient(#fff,#1c1c1c 50%,#fff)"></div><h3>Product Name</h3><p>Morbi diam mauris viverra in gravid</p><span class="price">£57.58</span><span class="cart">Add to Cart</span></div>
</div>

<footer class="abs footer">
  <div class="col" style="left:123px"><h4>COMPANY</h4><ul><li>Abou Us</li><li>Our Store</li><li>Jobs</li><li>Terms and Conditions</li><li>Site Map</li></ul></div>
  <div class="col" style="left:228px"><h4>PRODUCTS</h4><ul><li>Shipping and Delivery</li><li>Payment Methods</li><li>Return</li><li>Service</li><li>Help</li></ul></div>
  <div class="col" style="left:333px"><h4>SUPPORT</h4><ul><li>FAQs</li><li>Privacy Policy</li><li>Recommendations</li><li>Contact</li></ul></div>
  <div class="col news" style="left:434px"><h4>NEWSLETTER SIGN UP</h4><p>Please sign up here for latest deals</p><div class="field">Email address</div><div class="btn">SUBSCRIBE</div></div>
</footer>
<div class="abs bar">
  <small>© 2015 Company Name  All right reserved  Term of Use</small>
  <div class="social"><span></span><span></span><span></span></div>
</div>

</body>
</html>
```